Hi I'd like a book cover design that sits in between these two. The story is a love triangle and it is the second in the trilogy. It is one girl and two boys - aged around 21 and at college in the UK. I have included book 1 and 3 and would like a similar style. The book is called Turning Over , Perrick Lane Book 2. The author is Maddie Crosby.

Target Market(s)

new adult

Colors

Designer to choose colors to be used in the design.

Requirements
Must have
• girl is blonde, one man is blonde, the other dark haired
Nice to have
• arty style like the others. Not too rude!
Should not have
• Prefer not grey scale

```html
<!DOCTYPE html>
<html lang="en">
<head>
<meta charset="utf-8">
<title>Turning Over – Perrick Lane Book 2</title>
<link href="https://fonts.googleapis.com/css2?family=Playball&family=Cinzel:wght@500&family=Playfair+Display:wght@600&display=swap" rel="stylesheet">
<style>
  :root {
    --ink: #07090a;
    --deep-teal: #123a3c;
    --teal: #2a6a6a;
    --copper: #8a4a30;
    --rose: #5a3034;
    --frame: #b9a98a;
    --title: #ffffff;
    --gold: #f3e2a2;
    --gold-deep: #c9a95a;
  }
  html, body {
    margin: 0;
    padding: 0;
    overflow: hidden;
    background: var(--ink);
  }
  .cover {
    position: relative;
    width: 873px;
    height: 1200px;
    overflow: hidden;
    background:
      radial-gradient(ellipse at 15% 30%, rgba(42,106,106,.3), transparent 55%),
      radial-gradient(ellipse at 85% 70%, rgba(138,74,48,.3), transparent 55%),
      var(--ink);
  }
  .artwork {
    position: absolute;
    left: 42px;
    top: 44px;
    width: 785px;
    height: 1109px;
    box-sizing: border-box;
    border: 2px solid var(--frame);
    box-shadow: 0 0 18px rgba(0,0,0,.9);
    background: #0c0b0a;
  }
  .artwork svg {
    display: block;
    width: 100%;
    height: 100%;
  }
  .title {
    position: absolute;
    margin: 0;
    font-family: "Playball", cursive;
    font-weight: 400;
    color: var(--title);
    text-shadow: 3px 4px 2px rgba(0,0,0,.85);
    line-height: 1;
    white-space: nowrap;
  }
  .title-line-1 { left: 104px; top: 214px; font-size: 150px; }
  .title-line-2 { left: 512px; top: 402px; font-size: 150px; }
  .series {
    position: absolute;
    left: 0;
    width: 873px;
    text-align: center;
    font-family: "Cinzel", serif;
    font-weight: 500;
    color: var(--gold);
    background: linear-gradient(180deg, var(--gold), var(--gold-deep));
    -webkit-background-clip: text;
    background-clip: text;
    -webkit-text-fill-color: transparent;
    filter: drop-shadow(2px 2px 1px rgba(0,0,0,.8));
    line-height: 1;
    white-space: nowrap;
  }
  .series-name { top: 614px; font-size: 78px; padding-left: 8px; }
  .series-number { top: 718px; font-size: 68px; padding-left: 64px; }
  .author {
    position: absolute;
    left: 0;
    top: 1062px;
    width: 873px;
    text-align: center;
    font-family: "Playfair Display", serif;
    font-weight: 600;
    font-size: 50px;
    color: var(--title);
    text-shadow: 2px 2px 2px rgba(0,0,0,.8);
    line-height: 1;
  }
</style>
</head>
<body>
  <main class="cover">
    <div class="artwork">
      <svg viewBox="0 0 785 1109" preserveAspectRatio="none" role="img" aria-label="Artwork: glowing edge-lit painting of a blonde young woman between a blonde and a dark-haired young man, in teal and copper tones on black">
        <defs>
          <radialGradient id="glow-teal-left" cx="0.22" cy="0.22" r="0.4">
            <stop offset="0" stop-color="var(--teal)" stop-opacity=".85"/>
            <stop offset="1" stop-color="var(--teal)" stop-opacity="0"/>
          </radialGradient>
          <radialGradient id="glow-teal-right" cx="0.75" cy="0.25" r="0.38">
            <stop offset="0" stop-color="var(--deep-teal)" stop-opacity=".95"/>
            <stop offset="1" stop-color="var(--deep-teal)" stop-opacity="0"/>
          </radialGradient>
          <radialGradient id="glow-copper-centre" cx="0.5" cy="0.55" r="0.45">
            <stop offset="0" stop-color="var(--copper)" stop-opacity=".7"/>
            <stop offset="1" stop-color="var(--copper)" stop-opacity="0"/>
          </radialGradient>
          <radialGradient id="glow-rose-low" cx="0.3" cy="0.78" r="0.4">
            <stop offset="0" stop-color="var(--rose)" stop-opacity=".7"/>
            <stop offset="1" stop-color="var(--rose)" stop-opacity="0"/>
          </radialGradient>
          <linearGradient id="fade-bottom" x1="0" y1="0" x2="0" y2="1">
            <stop offset="0.6" stop-color="#050505" stop-opacity="0"/>
            <stop offset="1" stop-color="#050505" stop-opacity=".9"/>
          </linearGradient>
        </defs>
        <rect class="art-base" width="785" height="1109" fill="#14110f"/>
        <rect width="785" height="1109" fill="url(#glow-teal-left)"/>
        <rect width="785" height="1109" fill="url(#glow-teal-right)"/>
        <rect width="785" height="1109" fill="url(#glow-copper-centre)"/>
        <rect width="785" height="1109" fill="url(#glow-rose-low)"/>
        <rect width="785" height="1109" fill="url(#fade-bottom)"/>
      </svg>
    </div>
    <h1 class="title title-line-1">Turning</h1>
    <div class="title title-line-2">Over</div>
    <div class="series series-name">Perrick Lane</div>
    <div class="series series-number">Book 2</div>
    <div class="author">Maddie Crosby</div>
  </main>
</body>
</html>
```